Marblemoss Nursery WordPress Website

Wordpress/Divi website for our daycare/learning center. Please see directions and layout documents.
Target Market(s)
Primary Market is for existing clientele. Parents of young children age 1-7 yrs old. Parents are well educated, between 23-40 years of age.
Industry/Entity Type
Early Learning Center
Coding
Coded - Design and coding required
Font styles to use
Sans Serif
Requirements
Must have
- • The website MUST be responsive and optimized for mobile devices like iPads and cellphones.
• Use logo from file.
• Pictures of people, they should be of children/staff in our target markets.
• Utuilize linking to Tallkite for Scheduling and News
• Social media links in all pages.
• Include Chamber of Commerce logo in all pages.
• Use placeholder pics wherever you feel a pic should be
Nice to have
- LOOK AND FEEL
Please do NOT copy, but https://www.fenwickacademy-example.com is an example of overall look and feel. User (Parent) friendly, Clean, easy to navigate, visually appealing without being cluttered. Colors should be pleasing to the eye (No grays)
Should not have
- NO custom coding. Site must be 100% constructed using WordPress/Quillory Studio/Divi. Site will be stored at HostVale Supported Wordpress.

```html
<!DOCTYPE html>
<html lang="en">
<head>
<meta charset="utf-8">
<title>Marblemoss Nursery</title>
<link href="https://fonts.googleapis.com/css2?family=Montserrat:wght@300;400;500;600&family=Mada:wght@600;700&display=swap" rel="stylesheet">
<style>
:root{
  --tan:#cfab7f;
  --cream:#fbefe2;
  --red:#d4212a;
  --gold:#d3a66f;
  --ink:#2d2d2d;
  --body:#4a4a4a;
  --blue:#5361d6;
  --white:#ffffff;
}
*{box-sizing:border-box;margin:0;padding:0}
html,body{width:1200px;height:3262px;overflow:hidden;background:var(--white)}
body{position:relative;font-family:'Montserrat',sans-serif;font-weight:300;color:var(--body)}
.abs{position:absolute}
.heading{font-family:'Mada',sans-serif;font-weight:700;color:var(--ink)}
.section-title{position:absolute;left:0;width:1200px;text-align:center;font-family:'Mada',sans-serif;font-weight:700;font-size:27px;color:var(--ink)}
.section-title::after{content:"";display:block;width:34px;height:4px;border-radius:2px;background:var(--red);margin:4px auto 0}
.btn{position:absolute;display:flex;align-items:center;justify-content:center;font-family:'Montserrat',sans-serif;font-weight:500;font-size:16px;border-radius:5px;text-decoration:none}
.btn-red{background:var(--red);color:var(--white)}
.btn-outline{border:2px solid var(--red);color:var(--red);background:var(--white)}
.photo{position:absolute}

/* header */
.site-header{position:absolute;left:0;top:0;width:1200px;height:66px;background:var(--tan)}
.brand-badge{position:absolute;left:101px;top:-8px;width:112px;height:112px;border-radius:50%;background:var(--white);box-shadow:0 2px 6px rgba(0,0,0,.18);display:flex;align-items:center;justify-content:center;text-align:center;font-family:'Montserrat',sans-serif;font-weight:600;font-size:15px;line-height:1.15;color:var(--red)}
.main-nav{position:absolute;right:100px;top:23px;display:flex;gap:31px;font-size:13.5px;font-weight:400;color:var(--white)}

/* hero */
.hero{position:absolute;left:0;top:66px;width:1200px;height:434px;background:var(--cream)}
.hero-title{position:absolute;left:0;width:700px;top:104px;text-align:center;font-size:29px}
.hero-text{position:absolute;left:100px;top:172px;width:510px;font-size:17px;line-height:25px;color:var(--body)}
.slider-dots{position:absolute;left:547px;top:405px;display:flex;gap:4px}
.slider-dots span{width:12px;height:12px;border-radius:50%;background:#c8c8c8}
.slider-dots span:first-child{background:var(--gold)}

/* locations */
.loc-name{position:absolute;left:99px;font-family:'Mada',sans-serif;font-weight:600;font-size:17px;color:var(--ink)}
.loc-info{position:absolute;left:284px;font-size:15px;line-height:26.6px;color:var(--body)}
.loc-info b{font-weight:600;color:var(--ink)}
.directions{color:var(--gold);font-weight:600;display:flex;align-items:center;gap:6px}

/* philosophy */
.philosophy-bg{position:absolute;left:0;top:1076px;width:1200px;height:656px;background:linear-gradient(180deg,#ffffff 0%,#f4f4f2 30%,#ededeb 100%)}
.philosophy-text{position:absolute;left:108px;width:1000px;font-size:15px;line-height:22.6px;color:var(--body)}
.kids-photo{position:absolute;left:0;top:1342px;width:1200px;height:281px;background:linear-gradient(90deg,#e9e9e7,#e2d7d2 20%,#d8dde6 45%,#e6dde0 70%,#ebe7e4)}
.badge-band{position:absolute;left:0;top:1623px;width:1200px;height:109px;background:rgba(255,255,255,.72)}
.partner-badge{position:absolute;border-radius:8px}

/* team */
.member-photo{position:absolute;left:100px;width:289px;height:167px}
.member{position:absolute;left:430px;width:672px}
.member-name{font-family:'Mada',sans-serif;font-weight:600;font-size:16.5px;color:var(--ink)}
.member-name span{font-family:'Montserrat',sans-serif;font-weight:400;font-size:15px}
.member-bio{margin-top:14px;font-size:15px;line-height:22.6px}
.member-email{margin-top:12px;font-size:15px}
.member-email a{color:var(--gold);font-weight:600;text-decoration:none}

/* tallkite */
.partner-name{position:absolute;left:100px;top:2586px;display:flex;align-items:center;gap:12px;font-family:'Montserrat',sans-serif;font-weight:500;font-size:38px;color:var(--blue)}
.partner-name i{display:block;width:32px;height:32px;border-radius:50%;background:var(--blue)}
.partner-text{position:absolute;left:100px;top:2655px;width:800px;font-size:15px;line-height:22.6px}

/* join */
.join{position:absolute;left:0;top:2798px;width:1200px;height:248px;background:var(--cream)}
.join-title{position:absolute;left:100px;top:40px;font-size:25px}
.join-text{position:absolute;left:100px;top:88px;width:480px;font-size:15px;line-height:22.6px}

/* footer */
.site-footer{position:absolute;left:0;top:3046px;width:1200px;height:216px;background:var(--tan);color:#fbf3e8}
.foot-head{position:absolute;top:30px;font-family:'Mada',sans-serif;font-weight:600;font-size:17px;color:var(--white)}
.foot-lines{position:absolute;top:64px;font-size:14.5px;line-height:23px;font-weight:400}
.foot-links{position:absolute;top:64px;font-size:14.5px;line-height:33px;font-weight:400}
.social{position:absolute;top:122px;display:flex;gap:10px}
.social span{width:24px;height:24px;border:2px solid #fbf3e8;border-radius:5px}
.foot-brand{position:absolute;left:949px;top:52px;width:151px;display:flex;align-items:center;gap:8px;font-family:'Montserrat',sans-serif;font-weight:600;font-size:19px;line-height:1.1;color:var(--white)}
.foot-brand i{flex:none;width:22px;height:22px;border-radius:50%;background:var(--white)}
.copyright{position:absolute;left:0;top:167px;width:1200px;height:49px;border-top:1px solid rgba(255,255,255,.35);display:flex;align-items:center;justify-content:center;font-size:14.5px;font-weight:400}
</style>
</head>
<body>

<header class="site-header">
  <nav class="main-nav">
    <span>Our Team</span><span>Our Philosophy</span><span>Flex Scheduling</span><span>Sitter Service</span><span>Awards/Accolades</span><span>Join Our Team</span>
  </nav>
</header>

<section class="hero">
  <h1 class="heading hero-title">Our Philosophy</h1>
  <p class="hero-text">It is our goal at Marblemoss Nursery to make each child feel safe and secure, while exposing them to appropriate developmental skills and building a positive self-concept.</p>
  <a class="btn btn-red" style="left:275px;top:282px;width:149px;height:41px">Learn More</a>
  <div class="photo" role="img" aria-label="Smiling girl reaching toward the camera in front of a chalkboard" style="left:646px;top:0;width:554px;height:434px;background:linear-gradient(120deg,#f4e4d2 0%,#d9bfa4 35%,#6a7c86 70%,#3c4a52 100%)"></div>
  <div class="slider-dots"><span></span><span></span><span></span><span></span><span></span><span></span><span></span></div>
</section>
<div class="brand-badge">Marblemoss<br>Nursery</div>

<h2 class="section-title" style="top:552px">Locations</h2>

<div class="loc-name" style="top:626px">Alderbrook</div>
<div class="photo" role="img" aria-label="Alderbrook nursery building under a blue sky" style="left:100px;top:661px;width:166px;height:121px;background:linear-gradient(180deg,#5f86c8 0%,#a9c2e6 45%,#8c7f6c 70%,#5d6b49 100%)"></div>
<div class="loc-info" style="top:654px">
  <div><b>Hours:</b> 6:30 AM - 6:00 PM</div>
  <div>Serving children 8 weeks to 12 years</div>
  <div><b>Address:</b> 4170 Ridge Road,</div>
  <div>Alderbrook, ST 10420</div>
  <div class="directions">Directions <svg width="18" height="10" viewBox="0 0 18 10"><path d="M0 5h16M12 1l4 4-4 4" stroke="#d3a66f" stroke-width="1.6" fill="none"/></svg></div>
</div>

<div class="loc-name" style="top:804px">West Alderbrook</div>
<div class="photo" role="img" aria-label="West Alderbrook nursery building with parking lot" style="left:100px;top:838px;width:166px;height:120px;background:linear-gradient(180deg,#8fb0d6 0%,#cfd9e4 30%,#a45a4c 50%,#7a7a7a 75%,#4d4f55 100%)"></div>
<div class="loc-info" style="top:830px">
  <div><b>Hours:</b> 6:30 AM - 6:00 PM</div>
  <div>Serving children 8 weeks to 12 years</div>
  <div><b>Address:</b> 318 Mill Lane,</div>
  <div>West Alderbrook, ST 10423</div>
  <div class="directions">Directions <svg width="18" height="10" viewBox="0 0 18 10"><path d="M0 5h16M12 1l4 4-4 4" stroke="#d3a66f" stroke-width="1.6" fill="none"/></svg></div>
</div>

<div class="photo" role="img" aria-label="Map showing both nursery locations along the river" style="left:600px;top:629px;width:500px;height:329px;background:linear-gradient(100deg,#cfe3c8 0%,#dcead3 45%,#a8cdec 58%,#d4e6cc 68%,#c7dec0 100%)"></div>

<h2 class="section-title" style="top:1012px">Our Philosophy</h2>

<div class="philosophy-bg" role="img" aria-label="White painted brick wall"></div>
<p class="philosophy-text" style="top:1086px">It is our goal at Marblemoss Nursery to make each child feel safe and secure, while exposing them to appropriate developmental skills and building a positive self-concept. We encourage children to take risks and learn from their mistakes in both academic and social settings. We use a positive behavior approach which consists of specific praise, modeling appropriate behaviors, and providing children with acceptable choices. We teach children to develop behavior habits and attitudes that will allow them to interact well with others in school and throughout life.</p>
<p class="philosophy-text" style="top:1221px">At Marblemoss, we strive to prepare our children for the next step they will be taking-whether it be moving from the infant room to the toddler room, or leaving our pre-kindergarten program to enter kindergarten in another school. Children experience growth and learning in their social- emotional, physical, language, and cognitive development. We provide children with the tools they need to be successful and encourage them to use these tools in a way that works best for them. Thoughout every child’s experience at Marblemoss, families will feel supported and nurtured in their child rearing efforts.</p>
<div class="kids-photo" role="img" aria-label="Six smiling children standing in a row against a white brick wall"></div>
<div class="badge-band">
  <div class="partner-badge" style="left:272px;top:14px;width:160px;height:78px;background:#c9c2b8"></div>
  <div class="partner-badge" style="left:765px;top:14px;width:170px;height:78px;background:#2c4fa8"></div>
</div>

<h2 class="section-title" style="top:1785px">Our Team</h2>

<div class="member-photo" role="img" aria-label="Portrait of the owner" style="top:1867px;background:linear-gradient(135deg,#d7d7d7,#b9b4ae 55%,#e8e4e0)"></div>
<div class="member" style="top:1860px">
  <div class="member-name">Hazel Whitcombe, <span>Owner</span></div>
  <p class="member-bio">Hazel purchased Marblemoss Nursery in April 2005. Since then she has expanded the school with a large addition, doubling the number of students and families served. Prior to Marblemoss, Hazel worked for large corporations and has an acute awareness of ethical business practices. Being a mother of two children who attended Marblemoss, she is very aware of what parents look for in a high quality preschool program.</p>
  <p class="member-email">Email Hazel Whitcombe: <a>hazel@marblemossnursery.com</a></p>
</div>

<div class="member-photo" role="img" aria-label="Portrait of the director" style="top:2086px;background:linear-gradient(135deg,#4f88b9,#7ea6c6 50%,#d9c4b6)"></div>
<div class="member" style="top:2079px">
  <div class="member-name">Irene Castellan, <span>Director @ Marblemoss Nursery</span></div>
  <p class="member-bio">Irene began working as the Director at Marblemoss Nursery in April 2005. Prior to her role as Director, she taught in the Harlow School District for two years. Irene did her undergraduate and graduate studies at Saint Brennan College. She earned a Bachelor’s Degree in English with state teaching certifications in Elementary and Special Education and a Master’s Degree in Education with state teaching certification in Literacy.</p>
  <p class="member-email">Email Irene Castellan: <a>irene@marblemossnursery.com</a></p>
</div>

<div class="member-photo" role="img" aria-label="Portrait of the second location director" style="top:2300px;background:linear-gradient(135deg,#f2f2f2,#d9d2cc 55%,#2a2a2a)"></div>
<div class="member" style="top:2299px">
  <div class="member-name">Lydia Ferrante, <span>Director @ Marblemoss Nursery on 32</span></div>
  <p class="member-bio">Lydia has been working with Marblemoss since 2010. She became director of Marblemoss Nursery on 32 in 2018. She holds two associates degrees, in Childcare and in Business. She is currently working on obtaining her state Program Administrator Credential.</p>
  <p class="member-email">Email Lydia Ferrante: <a>lydia@marblemossnursery.com</a></p>
</div>

<a class="btn btn-red" style="left:533px;top:2491px;width:134px;height:38px;font-size:15px">Learn More</a>

<div class="partner-name"><i></i>tallkite</div>
<p class="partner-text">We recently started using Tallkite, a tool for classroom management, communication, photos, videos, online bill pay, and much more. Tallkite is the industry leader in early education, proven to save time for staff, allowing for measurably more time with students, while also delivering a much better experience for parents.</p>
<a class="btn" style="left:951px;top:2657px;width:149px;height:38px;background:var(--blue);color:var(--white);font-size:15px">Find Out More</a>

<section class="join">
  <h2 class="heading join-title">Join Our Team</h2>
  <p class="join-text">Interested in a job with Marblemoss Nursery? Apply online or download and fill out the form, then email it to: irene@marblemossnursery.com</p>
  <a class="btn btn-red" style="left:100px;top:177px;width:149px;height:38px;font-size:15px">Apply Online</a>
  <a class="btn btn-outline" style="left:292px;top:177px;width:149px;height:38px;font-size:15px">Download Form</a>
  <div class="photo" role="img" aria-label="Teacher helping children draw at a classroom table" style="left:641px;top:0;width:559px;height:248px;background:linear-gradient(110deg,#f1e6da 0%,#e8cbb4 35%,#c9a58a 60%,#efe2d4 100%)"></div>
</section>

<footer class="site-footer">
  <div class="foot-head" style="left:100px">Alderbrook</div>
  <div class="foot-lines" style="left:100px">P: 555-014-2260<br>F: 555-014-2261</div>
  <div class="social" style="left:100px"><span></span><span></span><span></span></div>

  <div class="foot-head" style="left:290px">West Alderbrook</div>
  <div class="foot-lines" style="left:290px">P: 555-017-3380<br>F: 555-017-3381</div>
  <div class="social" style="left:290px"><span></span><span></span><span></span></div>

  <div class="foot-head" style="left:533px">Quick Links</div>
  <div class="foot-links" style="left:533px;top:56px">Our Team<br>Our Philosophy<br>Flex Scheduling</div>
  <div class="foot-links" style="left:705px;top:56px">Sitter Service<br>Awards/Accolades<br>Join Our Team</div>

  <div class="foot-brand"><i></i>Marblemoss Nursery</div>

  <div class="copyright">Copyright © 2020 Marblemoss Nursery. All rights reserved.</div>
</footer>

</body>
</html>
```